7K Ventures business cards for a tech VC

We're starting a new Venture Capital that is focusing on bringing the best start ups from Israel to NYC
We need a business cards template for this that gives the sense of an entrepreneurial look
I don't want any religious signs on this even thought it's Israel
I'm looking for a techi feeling but not too crazy
The card should probably be in the same light blue as the logo and the logo in white

Target Market(s)

Investors

Industry/Entity Type

Tech

Contact Information for Business Card

The card needs to look slick and entrepreneurship like
The VC is focused on NYC and Tel Aviv so could be great to show something on the back side that is like NYC skyline or something like that
You can see the logo attached

Colors
0455a3
3276b5
85acd3
cedeed
eaf1f7

Requirements
Must have
• A very cool looking business card that shows we're a cutting edge tech VC with a focus on bringing start ups from Tel Aviv and leveraging the NYC ecosystem
Nice to have
• NYC skyline can be cool , maybe something that is connected to Tel Aviv

```html
<!DOCTYPE html>
<html lang="en">
<head>
<meta charset="utf-8">
<title>7K Ventures — Business Cards</title>
<link rel="stylesheet" href="https://fonts.googleapis.com/css2?family=Lato:wght@400;700;900&display=swap">
<style>
  :root {
    --bg: #2b2b2d;
    --card-blue: #2a8fd0;
    --brand-blue: #1f6fb5;
    --name-blue: #1d5ea8;
    --skyline-blue: #2a8fd0;
    --paper: #ffffff;
    --shadow: rgba(0, 0, 0, 0.45);
  }
  * { box-sizing: border-box; margin: 0; padding: 0; }
  html, body { width: 1200px; height: 880px; overflow: hidden; }
  body {
    background: var(--bg);
    font-family: "Lato", sans-serif;
    position: relative;
  }
  .card {
    position: absolute;
    width: 600px;
    height: 343px;
    box-shadow: 0 18px 40px var(--shadow);
    overflow: hidden;
  }
  /* Front */
  .card-front {
    left: 90px; top: 80px;
    background: var(--card-blue);
    display: flex; flex-direction: column;
    align-items: center; justify-content: center;
    color: var(--paper);
  }
  .brand {
    display: flex; align-items: center; gap: 14px;
    font-weight: 900; letter-spacing: 1px;
  }
  .brand-mark { width: 22px; height: 22px; background: currentColor; }
  .card-front .brand { font-size: 52px; }
  .card-front .brand-mark { width: 34px; height: 34px; }
  .front-web { margin-top: 22px; font-size: 17px; letter-spacing: 0.5px; }

  /* Back */
  .card-back {
    left: 510px; top: 460px;
    background: var(--paper);
  }
  .card-back .brand {
    position: absolute; right: 34px; top: 40px;
    font-size: 36px; color: var(--brand-blue);
  }
  .person { position: absolute; left: 36px; top: 96px; color: var(--name-blue); }
  .person-name { font-size: 24px; font-weight: 900; letter-spacing: 0.5px; }
  .person-role { font-size: 16px; }
  .contacts { position: absolute; left: 36px; top: 160px; list-style: none; }
  .contacts li {
    display: flex; align-items: center; gap: 9px;
    font-size: 15px; color: var(--name-blue); line-height: 22px;
  }
  .contacts svg { width: 16px; height: 16px; flex: none; }
  .skyline {
    position: absolute; left: 0; right: 0; bottom: 0; height: 112px;
    background: linear-gradient(180deg, #3a9ad8 0%, var(--skyline-blue) 100%);
  }
  .address {
    position: absolute; right: 30px; bottom: 20px;
    color: var(--paper); font-size: 15px; font-weight: 700; letter-spacing: 0.3px;
  }
</style>
</head>
<body>
  <section class="card card-front" aria-label="Card front">
    <div class="brand"><span class="brand-mark"></span>7K Ventures</div>
    <p class="front-web">www.7kventures.co</p>
  </section>

  <section class="card card-back" aria-label="Card back">
    <div class="brand"><span class="brand-mark"></span>7K Ventures</div>

    <div class="person">
      <p class="person-name">NOA LEVIN</p>
      <p class="person-role">Managing Partner</p>
    </div>

    <ul class="contacts">
      <li>
        <svg viewBox="0 0 16 16" aria-hidden="true"><rect width="16" height="16" rx="2" fill="#1d5ea8"/><path d="M4.5 3.5l2 2-1 1.2a6 6 0 0 0 3.8 3.8l1.2-1 2 2-1.2 1.2C7.5 12.5 3.5 8.5 3.3 4.7z" fill="#fff"/></svg>
        (212) 555 0147
      </li>
      <li>
        <svg viewBox="0 0 16 16" aria-hidden="true"><rect width="16" height="16" rx="2" fill="#1d5ea8"/><rect x="3" y="4.5" width="10" height="7" fill="none" stroke="#fff" stroke-width="1.2"/><path d="M3 4.5l5 4 5-4" fill="none" stroke="#fff" stroke-width="1.2"/></svg>
        hello@7kventures.co
      </li>
      <li>
        <svg viewBox="0 0 16 16" aria-hidden="true"><rect width="16" height="16" rx="2" fill="#1d5ea8"/><circle cx="8" cy="8" r="5" fill="none" stroke="#fff" stroke-width="1.1"/><ellipse cx="8" cy="8" rx="2.2" ry="5" fill="none" stroke="#fff" stroke-width="1"/><path d="M3 8h10" stroke="#fff" stroke-width="1"/></svg>
        www.7kventures.co
      </li>
    </ul>

    <div class="skyline" role="img" aria-label="City skyline silhouette with Statue of Liberty in blue"></div>
    <p class="address">PO BOX 418 Harbor Lane, 5th Avenue New York, USA</p>
  </section>
</body>
</html>
```